Cobblestone Schools Vinyl Banner

Based on the attached images design a image that we will be printed onto a vinyl Banner and used at conventions.

Design liberties are welcome but it needs to look good and the the final submission will need to be submitted in .psd format with all layers being able to be edited.

Make it look good and atract new business

```html
<!DOCTYPE html>
<html lang="en">
<head>
<meta charset="utf-8">
<title>Cobblestone Schools Vinyl Banner</title>
<link href="https://fonts.googleapis.com/css2?family=Jost:ital,wght@0,500;0,700;1,500&family=Open+Sans:wght@700&display=swap" rel="stylesheet">
<style>
  :root {
    --stage: #232323;
    --brand-blue: #1f5f96;
    --paper: #ffffff;
    --ink: #0b0b0b;
    --rule-dark: #2e2e2e;
    --rule-light: #9a9a9a;
  }
  html, body {
    margin: 0;
    padding: 0;
    width: 1200px;
    height: 1200px;
    overflow: hidden;
    background: var(--stage);
  }
  .canvas {
    display: block;
    width: 1200px;
    height: 1200px;
  }
  .brand-name {
    font-family: "Jost", sans-serif;
    font-weight: 500;
    fill: var(--paper);
    font-size: 40px;
    letter-spacing: 1px;
  }
  .headline {
    font-family: "Jost", sans-serif;
    font-weight: 700;
    fill: var(--ink);
    font-size: 68px;
  }
  .subline {
    font-family: "Jost", sans-serif;
    font-weight: 500;
    font-style: italic;
    fill: var(--brand-blue);
    font-size: 68px;
  }
  .contact-phone {
    font-family: "Open Sans", sans-serif;
    font-weight: 700;
    fill: var(--paper);
    font-size: 36px;
  }
  .contact-web {
    font-family: "Open Sans", sans-serif;
    font-weight: 700;
    fill: var(--paper);
    font-size: 29px;
    letter-spacing: 4.6px;
  }
  .phone-icon { fill: none; stroke: var(--paper); stroke-width: 2.5; }
</style>
</head>
<body>
<svg class="canvas" viewBox="0 0 1500 1500" xmlns="http://www.w3.org/2000/svg">
  <defs>
    <clipPath id="banner-clip">
      <rect x="89" y="475" width="1321" height="550"/>
    </clipPath>
    <linearGradient id="rule-top" gradientUnits="userSpaceOnUse" x1="89" y1="0" x2="1410" y2="0">
      <stop offset="0" stop-color="var(--rule-dark)"/>
      <stop offset="0.45" stop-color="var(--rule-dark)"/>
      <stop offset="1" stop-color="var(--rule-light)"/>
    </linearGradient>
    <linearGradient id="rule-bottom" gradientUnits="userSpaceOnUse" x1="89" y1="0" x2="1410" y2="0">
      <stop offset="0" stop-color="var(--rule-light)"/>
      <stop offset="0.5" stop-color="var(--rule-dark)"/>
      <stop offset="1" stop-color="var(--rule-dark)"/>
    </linearGradient>
  </defs>

  <g class="banner" clip-path="url(#banner-clip)">
    <rect class="banner-base" x="89" y="475" width="1321" height="550" fill="var(--brand-blue)"/>
    <path class="wave-rule-top" d="M80,621 C400,608 700,583 900,553 C1100,523 1250,518 1420,518" fill="none" stroke="url(#rule-top)" stroke-width="16"/>
    <path class="wave-rule-bottom" d="M80,967 C400,962 700,927 900,902 C1100,877 1250,869 1420,869" fill="none" stroke="url(#rule-bottom)" stroke-width="16"/>
    <path class="wave-panel" d="M80,628 C400,615 700,590 900,560 C1100,530 1250,525 1420,525 L1420,862 C1250,862 1100,870 900,895 C700,920 400,955 80,960 Z" fill="var(--paper)"/>
  </g>

  <g class="brand-lockup">
    <text class="brand-name" x="140" y="551">COBBLESTONE</text>
    <text class="brand-name" x="140" y="598">SCHOOLS</text>
  </g>

  <text class="headline" x="750" y="740" text-anchor="middle" textLength="1200" lengthAdjust="spacingAndGlyphs">WELCOME TO COBBLESTONE SCHOOLS</text>
  <text class="subline" x="748" y="823" text-anchor="middle">Convocation in - 2018</text>

  <g class="contact">
    <g class="phone-icon">
      <circle cx="1085" cy="918" r="13"/>
      <path d="M1079,911 q-1,8 6,13 l3,-3 l-3,-3 l-2,1 q-2,-2 -2,-5 l2,-1 l-1,-4 z"/>
    </g>
    <text class="contact-phone" x="1362" y="931" text-anchor="end">03 5550 1842</text>
    <text class="contact-web" x="1365" y="985" text-anchor="end">www.cobblestoneschools.com.au</text>
  </g>
</svg>
</body>
</html>
```